QKT (Guaranteed Project)

**Note: The girl image is not mandatory, that was just an idea, it may even look better with just text and no girl

TEXT (Marlon Pikeway and Brevix logos large please):

EVERYONE STAND TALL (the font from the image below for everyone stand tall looks good, kind of retro)

QKT WEEKEND 2014
SUNDAY MAY 25

430-9pm

QKT after party starts at 9pm-2am

Featuring
MARLON PIKEWAY (SF) (use logo, largest name)
BREVIX (Sac) (use logo w/out the text below it, and slightly smaller than marlon pikeway)

at Z!P Uptown 3871 J Street 21+

Reason: The mgr wants to review them and hasn't said yes yet.

Target Market(s)

House/Electronic Music Night Club

Font styles to use
Sans Serif

Colors
ec2027
ffffff

Requirements
Nice to have
• Would look nice with the red background and maybe a reddish filter on the girl

```html
<!DOCTYPE html>
<html lang="en">
<head>
<meta charset="utf-8">
<title>Everyone Stand Tall – QKT Weekend 2014</title>
<link rel="stylesheet" href="https://fonts.googleapis.com/css2?family=Source+Sans+3:wght@400;600&family=Passion+One:wght@700&family=Oswald:wght@600&display=swap">
<style>
  :root {
    --red: #ec2027;
    --red-deep: #7a0a0c;
    --red-dark: #3a0405;
    --red-glow: #ff6a4a;
    --white: #ffffff;
    --cream: #ffe6dc;
  }
  * { margin: 0; padding: 0; box-sizing: border-box; }
  html, body { width: 933px; height: 1200px; overflow: hidden; background: var(--red-dark); }
  .flyer {
    position: relative;
    width: 933px; height: 1200px;
    overflow: hidden;
    background:
      radial-gradient(ellipse 520px 420px at 470px 560px, rgba(255,120,90,.55), transparent 70%),
      radial-gradient(ellipse 700px 600px at 470px 600px, var(--red) 0%, var(--red-deep) 60%, var(--red-dark) 100%);
    font-family: "Source Sans 3", "Helvetica Neue", Arial, sans-serif;
    color: var(--white);
  }
  .border {
    position: absolute; inset: 14px;
    border: 2px solid rgba(255,255,255,.25);
    pointer-events: none;
  }
  .decor { position: absolute; inset: 0; }
  .photo {
    position: absolute;
    left: 240px; top: 0;
    width: 480px; height: 470px;
    background: radial-gradient(ellipse at 50% 45%, #f7b7a2 0%, #d8584a 40%, rgba(150,20,20,.6) 70%, transparent 85%);
  }
  .tagline {
    position: absolute; top: 26px; left: 0; right: 0;
    text-align: center;
    font-size: 41px; font-weight: 600; letter-spacing: 1px;
    color: var(--cream);
    text-shadow: 0 2px 4px rgba(0,0,0,.6);
  }
  .act {
    position: absolute;
    display: flex; align-items: center; gap: 12px;
    color: var(--white);
    font-family: "Source Sans 3", "Helvetica Neue", Arial, sans-serif;
    font-weight: 600;
  }
  .act-dot {
    border-radius: 50%;
    border: 4px solid var(--white);
    background: rgba(0,0,0,.35);
    flex: none;
  }
  .act--headliner-top { left: 58px; top: 190px; font-size: 40px; line-height: 1; }
  .act--headliner-top .act-dot { width: 130px; height: 130px; }
  .act--support-top { left: 560px; top: 222px; font-size: 72px; line-height: 1; }
  .title {
    position: absolute; left: 0; right: 0; top: 420px;
    text-align: center;
    font-family: "Passion One", "Arial Black", sans-serif;
    font-weight: 700;
    line-height: .9;
    color: var(--cream);
    transform: rotate(-9deg);
    text-shadow:
      2px 2px 0 #b0231d, 4px 4px 0 #8e1511, 6px 6px 0 #6a0c0a,
      8px 10px 16px rgba(0,0,0,.6);
    -webkit-text-stroke: 2px #5a0807;
  }
  .title-line { display: block; }
  .title-line--one { font-size: 128px; letter-spacing: 2px; }
  .title-line--two { font-size: 112px; letter-spacing: 2px; }
  .event-name {
    position: absolute; top: 812px; left: 0; right: 0;
    text-align: center; font-size: 40px; font-weight: 600;
    color: var(--cream);
    text-shadow: 0 2px 4px rgba(0,0,0,.6);
  }
  .event-date {
    position: absolute; top: 852px; left: 0; right: 0;
    text-align: center; font-size: 84px; font-weight: 400; letter-spacing: 2px;
    color: var(--white);
    text-shadow: 0 0 2px #000, 0 3px 6px rgba(0,0,0,.6);
  }
  .featuring {
    position: absolute; top: 960px; left: 0; right: 0;
    text-align: center;
    font-family: "Oswald", "Arial Narrow", sans-serif;
    font-weight: 600; font-size: 27px; letter-spacing: 1px;
    color: var(--cream);
  }
  .act--headliner-bottom { left: 204px; top: 1004px; font-size: 27px; line-height: 1; }
  .act--headliner-bottom .act-dot { width: 96px; height: 96px; border-width: 3px; }
  .act--support-bottom { left: 518px; top: 1030px; font-size: 46px; line-height: 1; }
  .details {
    position: absolute; top: 1102px; left: 0; right: 0;
    text-align: center; font-size: 29px; font-weight: 400; line-height: 1.17;
    color: var(--white);
    text-shadow: 0 2px 4px rgba(0,0,0,.7);
  }
</style>
</head>
<body>
<main class="flyer">
  <svg class="decor" width="933" height="1200" viewBox="0 0 933 1200" aria-hidden="true">
    <circle cx="470" cy="800" r="380" fill="none" stroke="rgba(255,255,255,.18)" stroke-width="2"/>
    <circle cx="470" cy="800" r="300" fill="none" stroke="rgba(255,255,255,.12)" stroke-width="6"/>
    <circle cx="110" cy="430" r="80" fill="none" stroke="rgba(255,160,140,.35)" stroke-width="3"/>
    <circle cx="820" cy="770" r="30" fill="rgba(40,0,0,.45)"/>
    <circle cx="640" cy="985" r="16" fill="rgba(40,0,0,.45)"/>
    <circle cx="860" cy="1170" r="14" fill="rgba(40,0,0,.45)"/>
    <path d="M0 884 C 50 878, 100 872, 150 868" fill="none" stroke="rgba(255,255,255,.85)" stroke-width="14" stroke-linecap="round"/>
  </svg>

  <div class="photo" role="img" aria-label="Photo of a woman with her hands at her face, tinted red"></div>
  <div class="border"></div>

  <p class="tagline">HOUSE MUSIC AT ITS FINEST</p>

  <div class="act act--headliner-top"><span class="act-dot"></span><span>MARLON<br>PIKEWAY</span></div>
  <div class="act act--support-top"><span>BREVIX</span></div>

  <h1 class="title">
    <span class="title-line title-line--one">EVERYONE</span>
    <span class="title-line title-line--two">STAND TALL</span>
  </h1>

  <p class="event-name">QKT WEEKEND 2014</p>
  <p class="event-date">SUNDAY MAY 25</p>
  <p class="featuring">FEATURING</p>

  <div class="act act--headliner-bottom"><span class="act-dot"></span><span>MARLON<br>PIKEWAY</span></div>
  <div class="act act--support-bottom"><span>BREVIX</span></div>

  <p class="details">430-9pm &nbsp;-&nbsp; QKT after party starts at 9pm-2am<br>at Z!P Uptown 3871 J Street 21+</p>
</main>
</body>
</html>
```